Meadowbrook Care Clinic needs a newspaper ad design

We need a newspaper ad for our Care Clinic. We provide primary medical care, medicated addiction therapy, psychiatric care, and psychotherapy in person and would really like to promote our teletherapy. So I have attached our company logo as well.

```html
<!DOCTYPE html>
<html lang="en">
<head>
<meta charset="utf-8">
<title>Meadowbrook Care Clinic – Newspaper Ad</title>
<link href="https://fonts.googleapis.com/css2?family=Bitter:ital,wght@0,700;0,800;1,800&family=Libre+Baskerville:wght@400;700&display=swap" rel="stylesheet">
<style>
  :root{
    --navy:#114d98;
    --navy-text:#1b4f9e;
    --green:#7cc97e;
    --lavender:#8d96d2;
    --white:#ffffff;
    --backdrop:#8a8b8d;
  }
  html,body{margin:0;padding:0;overflow:hidden}
  body{width:916px;height:1200px;background:var(--backdrop);position:relative}
  .ad{position:absolute;left:28px;top:326px;width:860px;height:548px;background:var(--white);overflow:hidden;font-family:"Libre Baskerville",Georgia,serif}
  .ad-shapes{position:absolute;inset:0}
  .brand{position:absolute;left:34px;top:30px;display:flex;align-items:center;gap:10px}
  .brand-dot{width:30px;height:30px;border-radius:50%;background:var(--green);flex:none}
  .brand-name{font-size:25px;color:var(--navy-text);line-height:1}
  .brand-tagline{position:absolute;left:74px;top:68px;font-size:16px;color:#1c1c1c}
  .photo{position:absolute;border-radius:50%}
  .photo-care{left:433px;top:30px;width:394px;height:394px;background:radial-gradient(circle at 55% 55%,#d9b3a0 0%,#c79a86 30%,#3f86c9 62%,#2c6fb6 100%)}
  .photo-family{left:317px;top:237px;width:212px;height:212px;background:linear-gradient(135deg,#efe6dc 0%,#d8c2b4 45%,#7d7787 75%,#eab8c4 100%);box-shadow:0 0 0 6px var(--lavender)}
  .dot{position:absolute;border-radius:50%}
  .dot-green{left:526px;top:390px;width:68px;height:68px;background:var(--green)}
  .dot-lavender{left:584px;top:409px;width:44px;height:44px;background:var(--lavender);opacity:.75}
  .headline{position:absolute;left:39px;top:188px;margin:0;font-family:Bitter,Georgia,serif;font-weight:800;font-size:22px;line-height:21.6px;color:var(--white);text-transform:uppercase}
  .headline .accent{color:var(--green)}
  .services-title{position:absolute;left:39px;top:312px;margin:0;font-family:Bitter,Georgia,serif;font-style:italic;font-weight:800;font-size:18px;color:var(--white)}
  .services-rule{position:absolute;left:39px;top:348px;width:38px;height:2px;background:var(--white)}
  .services-rule::after{content:"";position:absolute;left:38px;top:0;width:40px;height:1px;background:rgba(255,255,255,.5)}
  .services{position:absolute;left:39px;top:357px;margin:0;padding:0;list-style:none;color:var(--white);font-size:17px;line-height:21.8px}
  .services li{display:flex;align-items:center;gap:5px}
  .tick{width:16px;height:16px;flex:none}
  .cta{position:absolute;left:37px;top:484px;width:510px;height:51px}
  .cta-text{position:absolute;left:18px;top:4px;font-family:Bitter,Georgia,serif;font-style:italic;font-weight:800;font-size:19px;line-height:21px;color:var(--white)}
  .cta-icon{position:absolute;left:193px;top:9px;width:34px;height:34px}
  .cta-phone{position:absolute;left:236px;top:7px;font-family:"Libre Baskerville",Georgia,serif;font-weight:700;font-size:28px;line-height:36px;color:var(--navy-text);white-space:nowrap}
  .location{position:absolute;left:589px;top:478px;display:flex;align-items:center;gap:7px;color:var(--white);font-size:14.5px}
  .location svg{width:12px;height:17px}
  .website{position:absolute;right:22px;top:501px;display:flex;align-items:center;gap:3px;color:var(--white);font-size:18px;white-space:nowrap}
  .website svg{width:24px;height:24px;flex:none}
</style>
</head>
<body>
<main class="ad">
  <svg class="ad-shapes" viewBox="0 0 860 548" aria-hidden="true">
    <path d="M0,160 C140,110 330,105 480,205 L560,330 C650,355 760,355 860,338 L860,548 L0,548 Z" fill="var(--navy)"/>
    <path d="M8,190 C140,125 320,85 520,200 C400,130 220,120 8,190 Z" fill="var(--green)"/>
    <path d="M700,380 C760,370 820,350 860,338 L860,400 C810,392 760,388 700,380 Z" fill="var(--green)"/>
    <path d="M660,360 C740,340 800,332 860,330 L860,338 C790,345 730,355 660,360 Z" fill="var(--lavender)"/>
  </svg>

  <div class="brand"><span class="brand-dot"></span><span class="brand-name">Meadowbrook Care Clinic</span></div>
  <div class="brand-tagline">Dedicated to Hope, Healing &amp; Recovery</div>

  <div class="photo photo-care" role="img" aria-label="Close-up of a nurse in blue scrubs holding an elderly patient's hands"></div>
  <div class="photo photo-family" role="img" aria-label="Mother and young daughter at a clinic visit with a clipboard"></div>
  <div class="dot dot-green"></div>
  <div class="dot dot-lavender"></div>

  <h1 class="headline"><span class="accent">Meadowbrook Care<br>Clinic</span> is a family<br>focused medical and<br>mental health care<br>practice.</h1>

  <h2 class="services-title">We provide</h2>
  <div class="services-rule"></div>
  <ul class="services">
    <li><svg class="tick" viewBox="0 0 16 16"><circle cx="8" cy="8" r="8" fill="var(--green)"/><path d="M4.3 8.2l2.4 2.4 5-5" fill="none" stroke="#fff" stroke-width="2"/></svg>Primary medical care</li>
    <li><svg class="tick" viewBox="0 0 16 16"><circle cx="8" cy="8" r="8" fill="var(--green)"/><path d="M4.3 8.2l2.4 2.4 5-5" fill="none" stroke="#fff" stroke-width="2"/></svg>Medicated addiction therapy</li>
    <li><svg class="tick" viewBox="0 0 16 16"><circle cx="8" cy="8" r="8" fill="var(--green)"/><path d="M4.3 8.2l2.4 2.4 5-5" fill="none" stroke="#fff" stroke-width="2"/></svg>Psychiatric care</li>
    <li><svg class="tick" viewBox="0 0 16 16"><circle cx="8" cy="8" r="8" fill="var(--green)"/><path d="M4.3 8.2l2.4 2.4 5-5" fill="none" stroke="#fff" stroke-width="2"/></svg>Psychotherapy in person</li>
    <li><svg class="tick" viewBox="0 0 16 16"><circle cx="8" cy="8" r="8" fill="var(--green)"/><path d="M4.3 8.2l2.4 2.4 5-5" fill="none" stroke="#fff" stroke-width="2"/></svg>And Teletherapy</li>
  </ul>

  <div class="cta">
    <svg width="510" height="51" viewBox="0 0 510 51" aria-hidden="true"><path d="M0,0 H510 L492,51 H0 Z" fill="var(--green)"/></svg>
    <div class="cta-text">Call for an<br>Appointment!</div>
    <svg class="cta-icon" viewBox="0 0 32 32" aria-hidden="true"><circle cx="16" cy="16" r="14.5" fill="none" stroke="#fff" stroke-width="2"/><path d="M10.5 9.5c1-.8 2-.6 2.6.4l1.3 2.3c.4.8.2 1.6-.5 2.1l-1 .7c.8 2 2.2 3.5 4.2 4.3l.8-1c.5-.7 1.3-.8 2.1-.4l2.2 1.4c.9.6 1.1 1.6.3 2.5-1.4 1.6-3.4 1.9-5.5.8-3.5-1.8-5.9-4.5-7.2-8-.7-2-.3-3.8.7-5.1z" fill="#fff"/><path d="M18 9.5a5 5 0 0 1 4.5 4.5M18 6.5a8 8 0 0 1 7.5 7.5" fill="none" stroke="#fff" stroke-width="1.5"/></svg>
    <div class="cta-phone">(555) 014-2290</div>
  </div>

  <div class="location"><svg viewBox="0 0 12 17" aria-hidden="true"><path d="M6 0a6 6 0 0 0-6 6c0 4.5 6 11 6 11s6-6.5 6-11a6 6 0 0 0-6-6zm0 8.5a2.5 2.5 0 1 1 0-5 2.5 2.5 0 0 1 0 5z" fill="#fff"/></svg>Located in Willow Creek, CO</div>
  <div class="website">www.meadowbrookcare.com<svg viewBox="0 0 26 26" aria-hidden="true"><path d="M11 9l12 5-5 1.5 4 5-2 1.6-4-5-3 4z" fill="var(--green)"/><path d="M9 3v4M3 9h4M4.5 4.5l2.8 2.8M13 4.5l-2.2 2.3M4.5 13l2.3-2.2" stroke="var(--green)" stroke-width="1.5"/></svg></div>
</main>
</body>
</html>
```